Business Card Design - Law Firm

I need a business card design. I have attached a picture of the law firm's website and logo. The business card design should be consistent with those pictures. There should be a place for the employee name, employee job title, telephone number, facsimile number, address, website url, and email address for each employee.
Industry/Entity Type
Business

```html
<!DOCTYPE html>
<html lang="en">
<head>
<meta charset="utf-8">
<title>Marlowe Law – Business Card</title>
<link rel="stylesheet" href="https://fonts.googleapis.com/css2?family=Arimo:wght@400;700&family=Sorts+Mill+Goudy&display=swap">
<style>
  :root {
    --backdrop: #e4e2df;
    --card-light: #ffffff;
    --card-shade: #ececec;
    --gold: #a98c45;
    --gold-band: #cfb06a;
    --ink: #2b2b2b;
    --mark: #2a2523;
    --icon: #a98c45;
  }
  * { box-sizing: border-box; margin: 0; padding: 0; }
  html, body { width: 1186px; height: 1200px; overflow: hidden; }
  body { background: var(--backdrop); position: relative; font-family: "Arimo", Arial, sans-serif; }

  .card {
    position: absolute;
    left: 152px;
    width: 901px;
    height: 512px;
    background: radial-gradient(ellipse at 55% 45%, var(--card-light) 40%, var(--card-shade) 100%);
    box-shadow: 0 4px 14px rgba(0,0,0,0.25);
    overflow: hidden;
  }
  .card--front { top: 67px; }
  .card--back { top: 627px; }

  .corner-band {
    position: absolute; left: 0; top: 0;
    width: 160px; height: 141px;
    background: var(--gold-band);
    clip-path: polygon(0 0, 100% 0, 0 100%);
  }

  .brand { position: absolute; display: flex; align-items: center; gap: 34px; }
  .brand__square { width: 66px; height: 66px; background: var(--mark); }
  .brand__name {
    font-family: "Sorts Mill Goudy", Georgia, serif;
    font-size: 62px; color: var(--gold); font-weight: 400; white-space: nowrap;
  }
  .card--front .brand { left: 207px; top: 108px; }
  .card--back .brand { left: 207px; top: 166px; }

  .person { position: absolute; left: 70px; top: 320px; width: 270px; text-align: center; }
  .person__name { font-size: 34px; font-weight: 700; color: var(--gold); white-space: nowrap; letter-spacing: -0.3px; }
  .person__title { font-size: 22px; color: var(--ink); margin-top: 8px; }

  .contacts { position: absolute; left: 450px; top: 270px; list-style: none; }
  .contacts li { display: flex; align-items: center; height: 36.5px; font-size: 25px; color: var(--ink); white-space: nowrap; }
  .contacts svg { width: 20px; height: 20px; margin-right: 10px; flex: none; }

  .web { position: absolute; left: 0; right: 0; top: 257px; text-align: center; font-size: 25px; color: var(--ink); padding-left: 130px; }
</style>
</head>
<body>
  <section class="card card--front">
    <div class="corner-band"></div>
    <div class="brand">
      <div class="brand__square"></div>
      <div class="brand__name">Marlowe Law</div>
    </div>
    <div class="person">
      <div class="person__name">Dana Marlowe</div>
      <div class="person__title">CEO</div>
    </div>
    <ul class="contacts">
      <li><svg viewBox="0 0 20 20" fill="var(--icon)"><path d="M4 2h8v16H4z M12 8h4v10h-4z"/><rect x="6" y="5" width="2" height="2" fill="#fff"/><rect x="6" y="10" width="2" height="2" fill="#fff"/></svg>PO Box 318, Larrakeyah, NT 0820</li>
      <li><svg viewBox="0 0 20 20" fill="none" stroke="var(--icon)" stroke-width="2"><path d="M4 3h4l2 4-2 2c1 2 2 3 4 4l2-2 4 2v4h-3C9 17 3 11 3 5V3z"/></svg>0431 608 275</li>
      <li><svg viewBox="0 0 20 20" fill="var(--icon)"><rect x="2" y="8" width="16" height="9" rx="1"/><rect x="5" y="3" width="10" height="5"/><rect x="5" y="11" width="10" height="2" fill="#fff"/></svg>0431 608 275</li>
      <li><svg viewBox="0 0 20 20" fill="none" stroke="var(--icon)" stroke-width="1.8"><rect x="2" y="4" width="16" height="12"/><path d="M2 4l8 7 8-7"/></svg>danamarlowe@marlowelaw.com</li>
      <li><svg viewBox="0 0 20 20" fill="none" stroke="var(--icon)" stroke-width="1.6"><circle cx="10" cy="10" r="8"/><ellipse cx="10" cy="10" rx="3.5" ry="8"/><path d="M2 10h16M4 5.5h12M4 14.5h12"/></svg>www.marlowelaw.com</li>
    </ul>
  </section>

  <section class="card card--back">
    <div class="corner-band"></div>
    <div class="brand">
      <div class="brand__square"></div>
      <div class="brand__name">Marlowe Law</div>
    </div>
    <div class="web">www.marlowelaw.com</div>
  </section>
</body>
</html>
```